Venture Keystone - Client Appreciation Party Invitation and Poster

We need a printable invitation, a version of the same invitation that can be emailed out, and also a Poster of the invitation for our annual client appreciation party.

The location is called: The Lanternhouse. Here is a link to the location: https://www.thelanternhousevenue.example/

We like their font and their little logo that you see when you log onto this page. But we'd love to see creatively what you can come up with.

This party is for our clients who are interior designers and owners in the Hospitality industry. Here are the details which need to be included in the invitation:

Location: The Lanternhouse - 482 W Brindle Ave. Chicago IL 60614
Date/Time: Thursday August 23rd - 5:30-9:00pm
RSVP: Please RSVP to: gathering@venturekeystone.example

Then our Sponsors Logos need to be included on the bottom: I have uploaded those logos here as well as our Logo and a copy of the invitation we did for last year's party so you can see sort of what we've done in the past.

For the poster - we typically do a version of the invitation (see uploaded example of last year's poster) with the sponsor logos and the overall theme of the invitation just a bit simplified by removing the date/time/location info. We need this in a printable format which can be blown up to a 24x30 poster size.

Requirements
Must have
• use 2 to 3 colors only.
• logos of sponsors can be of the same color.

```html
<!DOCTYPE html>
<html lang="en">
<head>
<meta charset="UTF-8">
<title>Venture Keystone – Weekend Warm Up Invitation</title>
<link rel="stylesheet" href="https://fonts.googleapis.com/css2?family=Ruslan+Display&family=Roboto:wght@400;700&display=swap">
<style>
  :root {
    --backdrop: #d3dadd;
    --lacquer-red: #ec2027;
    --gold: #f0c970;
    --lion-yellow: #fdd845;
    --lion-red: #c8161d;
  }
  * { box-sizing: border-box; margin: 0; padding: 0; }
  html, body {
    width: 1200px; height: 1200px; overflow: hidden;
    background: var(--backdrop);
  }
  .invitation {
    position: absolute; left: 140px; top: 25px;
    width: 920px; height: 1150px;
    background: var(--lacquer-red);
    color: var(--gold);
    font-family: "Roboto", Arial, sans-serif;
  }
  .frame-lines { position: absolute; inset: 0; width: 100%; height: 100%; }
  .centered {
    position: absolute; left: 0; right: 0; text-align: center; white-space: nowrap;
  }
  .host-name { top: 84px; font-size: 35px; letter-spacing: 1px; }
  .display {
    font-family: "Ruslan Display", "Roboto", sans-serif;
    line-height: 1;
  }
  .title-weekend { top: 128px; font-size: 110px; letter-spacing: 2px; }
  .title-warmup { top: 248px; font-size: 84px; letter-spacing: 1px; }
  .lion-mascot {
    position: absolute; left: 332px; top: 373px; width: 248px; height: 264px;
  }
  .event-type { top: 662px; font-size: 48px; letter-spacing: 2px; }
  .event-date { top: 746px; font-size: 34px; font-weight: 700; }
  .event-time { top: 798px; font-size: 34px; }
  .venue-box {
    position: absolute; left: 154px; top: 875px; width: 613px; height: 58px;
    border: 2px solid var(--gold);
    display: flex; align-items: center; justify-content: center;
    font-size: 22px; letter-spacing: 0.3px; white-space: nowrap;
  }
  .sponsors {
    position: absolute; left: 70px; right: 55px; top: 974px;
    display: flex; align-items: center; justify-content: space-between;
    font-size: 27px; white-space: nowrap;
  }
  .sponsor { display: flex; align-items: center; gap: 8px; }
  .sponsor-dot { width: 24px; height: 24px; border-radius: 50%; background: var(--gold); }
  .sponsor-square { width: 28px; height: 28px; background: var(--gold); }
  .rsvp-email { top: 1052px; font-size: 18px; }
</style>
</head>
<body>
  <main class="invitation">
    <svg class="frame-lines" viewBox="0 0 920 1150" aria-hidden="true">
      <g fill="none" stroke="var(--gold)" stroke-width="3">
        <rect x="33" y="40" width="854" height="1070"/>
        <rect x="50" y="22" width="820" height="1106" stroke-width="2"/>
        <path d="M33 120 A80 80 0 0 0 113 40"/>
        <path d="M887 120 A80 80 0 0 1 807 40"/>
        <path d="M33 1030 A80 80 0 0 1 113 1110"/>
        <path d="M887 1030 A80 80 0 0 0 807 1110"/>
      </g>
    </svg>

    <p class="centered host-name">VENTURE KEYSTONE</p>
    <h1 class="centered display title-weekend">WEEKEND</h1>
    <h2 class="centered display title-warmup">WARM UP</h2>

    <svg class="lion-mascot" viewBox="0 0 248 264" role="img" aria-label="Lion dance head mascot illustration">
      <defs>
        <linearGradient id="lionTones" x1="0" y1="0" x2="0" y2="1">
          <stop offset="0" stop-color="var(--lion-yellow)"/>
          <stop offset="0.6" stop-color="var(--lion-yellow)"/>
          <stop offset="1" stop-color="var(--lion-red)"/>
        </linearGradient>
      </defs>
      <rect x="0" y="0" width="248" height="264" rx="40" fill="url(#lionTones)"/>
    </svg>

    <p class="centered display event-type">CLIENT APPRECIATION EVENT</p>
    <p class="centered event-date">THURSDAY AUGUST 23rd</p>
    <p class="centered event-time">5:30-9:00PM</p>

    <div class="venue-box">The Lanternhouse - 482 W Brindle Ave. Chicago IL 60614</div>

    <div class="sponsors">
      <span class="sponsor"><span class="sponsor-dot"></span>Lumeora</span>
      <span class="sponsor"><span class="sponsor-square"></span>Vellmark</span>
      <span class="sponsor"><span class="sponsor-square"></span>Brightfold</span>
      <span class="sponsor">Harrow Hospitality</span>
    </div>

    <p class="centered rsvp-email">gathering@venturekeystone.example</p>
  </main>
</body>
</html>
```